Stationery and Business Card Design

We need stationary design for our new company larkvale. Larkvale is a company that provides city apartment rentals for tourists in Athens We need business cards, letterheads for A4 and A5 and envelopes for A4 A5. The design needs to be modern, friendly and corporate.

Target Market(s)

City Tourists

Industry/Entity Type

Tourism

```html
<!DOCTYPE html>
<html lang="en">
<head>
<meta charset="utf-8">
<title>Larkvale Business Card</title>
<link rel="stylesheet" href="https://fonts.googleapis.com/css2?family=Raleway:wght@400;500;600;700&display=swap">
<style>
  :root {
    --backdrop: #a9a6a7;
    --plum: #832157;
    --paper: #f6f6f6;
    --ink: #333333;
    --ink-soft: #555555;
    --charcoal: #3b3a3a;
  }
  * { margin: 0; padding: 0; box-sizing: border-box; }
  html, body {
    width: 1200px; height: 1200px; overflow: hidden;
    background: var(--backdrop);
    font-family: "Raleway", sans-serif;
  }
  .canvas { position: relative; width: 1200px; height: 1200px; }
  .card {
    position: absolute; border-radius: 22px; overflow: hidden;
  }
  .card-front {
    left: 238px; top: 117px; width: 714px; height: 420px;
    background: var(--plum);
  }
  .front-mark {
    position: absolute; left: 302px; top: 114px; width: 102px; height: 100px;
    background: #ffffff;
  }
  .front-name {
    position: absolute; left: 0; right: 0; top: 222px;
    text-align: center; color: #ffffff;
    font-size: 68px; font-weight: 400; letter-spacing: -0.5px;
  }
  .card-back {
    left: 231px; top: 645px; width: 711px; height: 415px;
    background: var(--paper);
  }
  .back-mark {
    position: absolute; left: 45px; top: 63px; width: 102px; height: 98px;
    background: var(--plum);
  }
  .back-name {
    position: absolute; left: 180px; top: 68px;
    color: var(--plum); font-size: 54px; font-weight: 400; letter-spacing: -0.5px;
  }
  .holder { position: absolute; left: 46px; top: 234px; }
  .holder-name { color: var(--plum); font-size: 26px; font-weight: 600; }
  .holder-title { color: var(--ink-soft); font-size: 18px; margin-top: 4px; }
  .contact { position: absolute; left: 370px; top: 234px; font-size: 18px; color: var(--ink); }
  .contact-row { display: flex; align-items: center; height: 24px; }
  .contact-row svg { width: 16px; height: 16px; margin-right: 18px; fill: var(--plum); }
  .accent { color: var(--plum); }
  .address { margin-top: 8px; line-height: 25px; color: var(--ink-soft); }
  .base-band { position: absolute; left: 0; bottom: 0; width: 711px; height: 20px; }
</style>
</head>
<body>
<main class="canvas">
  <section class="card card-front" aria-label="Card front">
    <div class="front-mark"></div>
    <div class="front-name">Larkvale</div>
  </section>

  <section class="card card-back" aria-label="Card back">
    <div class="back-mark"></div>
    <div class="back-name">Larkvale</div>

    <div class="holder">
      <div class="holder-name">John Smith</div>
      <div class="holder-title">Your Title</div>
    </div>

    <div class="contact">
      <div class="contact-row">
        <svg viewBox="0 0 16 16"><path d="M2 6c0-2 3-3 6-3s6 1 6 3v1h-3V5.5H5V7H2zM4 8h8l2 5H2z"/></svg>
        <span>+00 111 222 3333</span>
      </div>
      <div class="contact-row">
        <svg viewBox="0 0 16 16"><path d="M8 1a7 7 0 1 0 0 14A7 7 0 0 0 8 1zm0 1.5c.8 0 1.7 1.6 2 4H6c.3-2.4 1.2-4 2-4zM2.6 7.2h2.6v1.6H2.6zm8.2 0h2.6v1.6h-2.6zM6 9.5h4c-.3 2.4-1.2 4-2 4s-1.7-1.6-2-4z"/></svg>
        <span>www.<span class="accent">yourwebsite</span>.com</span>
      </div>
      <div class="contact-row">
        <svg viewBox="0 0 16 16"><path d="M1 3h14v10H1zm1.5 1.2L8 8.5l5.5-4.3z"/></svg>
        <span>yourname@yourwebsite.com</span>
      </div>
      <div class="address">Your Long Commercial or<br>business address in 2 line</div>
    </div>

    <svg class="base-band" viewBox="0 0 711 20" preserveAspectRatio="none">
      <rect x="0" y="2" width="711" height="18" fill="var(--charcoal)"/>
      <polygon points="0,2 510,2 475,20 0,20" fill="var(--plum)"/>
      <polygon points="510,2 530,2 485,20 470,20" fill="#ffffff"/>
    </svg>
  </section>
</main>
</body>
</html>
```